Plate Bright Workshop (workshop to teach people to eat fruits and vegetables)

Double sided DL Flyer

Free Community Workshop
Plate Bright Live Lively
Central Coast NSW

Copy to appear on flyer side one:-
PLATE BRIGHT LIVE LIVELY
interactive workshops
March-April 2019
Presented by qualified nutritionist

Food for healthier happier life for you and your family (free to central coast residents - all ages welcome

Side 2
Learn About:-
Foods that improve your health
basic nutrition
gut brain connection
portion size
menu planning
preparation
eating

Benefits
Improved health
Improved Energy
Manage chronic illness
diabetes type II
cholesterol
Blood Pressure
Family fun

Food Tastings
Lucky Door Prize

Reserve for spot online @ www.platebright.com.au or call 0462 508 731
Supported by Harbourline Shire Council (Logo) Harbourline Rugby Social Club (Logo) Pindara Veterans Club (Logo)

I would like to see a flyer that is bright, fun and fresh with images of fresh food.

Target Market(s)

Women 30 plus

Industry/Entity Type

Health And Wellness

Logo Text

PLATE BRIGHT LIVE LIVELY

Font styles to use
Other font styles liked:
• bold clean

Colors
f37122
9bcb3c
fbed22
ec1f27
e34297

Requirements
Must have
• bright eye catching colours featuring fresh fruit and vegetables
• I have attached a some images of designs I like
Nice to have
• Im happy for the designer to change copy to create a clean flyer without loosing essential information
• I like the feel of the banner on my facebook page
• Kindly Nourish - Plate Bright Live Lively with Megan Troute
• https://www.facebook.com/kindlynourishoz/
Should not have
• old fashioned images

```html
<!DOCTYPE html>
<html lang="en">
<head>
<meta charset="utf-8">
<title>Plate Bright Workshop – DL Flyer</title>
<link rel="stylesheet" href="https://fonts.googleapis.com/css2?family=Montserrat:wght@800;900&family=Quicksand:wght@500;600;700&family=Oswald:wght@500;600&display=swap">
<style>
:root{
  --bg:#4a4a4a;
  --green:#8cc21f;
  --green-light:#a6d33a;
  --green-dark:#6fa812;
  --pink:#ec1e8c;
  --red:#e31b23;
  --red-dark:#c0141b;
  --white:#ffffff;
  --ink:#111111;
  --text:#222222;
}
*{margin:0;padding:0;box-sizing:border-box}
html,body{width:1200px;height:1200px;overflow:hidden;background:var(--bg)}
.canvas{position:relative;width:1200px;height:1200px}
.flyer{position:absolute;top:178px;width:402px;height:845px;background:var(--white);overflow:hidden}
.flyer--front{left:157px}
.flyer--back{left:641px}
.layer{position:absolute;left:0;top:0}
.abs{position:absolute}
.brand{font-family:"Quicksand",sans-serif;font-weight:700;color:var(--green);font-size:21px;letter-spacing:.5px;white-space:nowrap}
.photo{position:absolute}

/* front */
.front-brand{left:156px;top:28px}
.fruit-photo{left:0;top:118px;width:402px;height:230px;background:radial-gradient(ellipse at 55% 50%,#9ad23a 0,#e8574a 35%,#f6d8cf 62%,#ffffff 85%)}
.portrait{left:211px;top:288px;width:172px;height:172px;border-radius:50%;border:5px solid var(--pink);background:radial-gradient(circle at 55% 40%,#f2e6e0 0,#c9b3a6 50%,#8a7a70 100%)}
.headline{left:24px;top:474px;font-family:"Montserrat",sans-serif;font-weight:900;color:var(--white);font-size:38px;line-height:36px;letter-spacing:.2px;white-space:nowrap}
.presenter{left:24px;top:598px;font-family:"Quicksand",sans-serif;font-weight:700;color:var(--ink);font-size:19.5px;white-space:nowrap}
.tagline{left:24px;top:628px;width:360px;font-family:"Quicksand",sans-serif;font-weight:600;color:var(--white);font-size:17.5px;line-height:21px}
.free-badge{left:24px;top:686px;width:353px;height:70px;border-radius:12px;background:linear-gradient(180deg,var(--red),var(--red-dark));color:var(--white);font-family:"Montserrat",sans-serif;font-weight:900;font-size:22.5px;line-height:26px;text-align:center;padding-top:9px;white-space:nowrap}
.welcome{left:0;width:402px;top:762px;text-align:center;font-family:"Quicksand",sans-serif;font-weight:600;color:var(--white);font-size:20px}
.site{left:0;width:402px;top:798px;text-align:center;font-family:"Quicksand",sans-serif;font-weight:700;color:var(--white);font-size:16px;display:flex;justify-content:center;align-items:center;gap:6px}

/* back */
.section-title{font-family:"Quicksand",sans-serif;font-weight:700;font-size:28px;white-space:nowrap}
.learn-title{left:24px;top:20px;color:var(--green)}
.bullets{list-style:none;font-family:"Quicksand",sans-serif;font-weight:500;color:var(--text);font-size:14.5px;line-height:17px}
.bullets li{position:relative;padding-left:13px;margin-bottom:7px}
.bullets li::before{content:"";position:absolute;left:1px;top:6px;width:4px;height:4px;border-radius:50%;background:var(--green)}
.learn-left{left:24px;top:58px;width:170px}
.learn-right{left:206px;top:58px}
.benefits{left:25px;top:155px;width:352px;height:143px;border-radius:16px;background:linear-gradient(160deg,var(--green-light),var(--green-dark))}
.benefits-title{left:12px;top:4px;color:var(--white)}
.benefits .bullets{color:var(--white);font-weight:700;font-size:14px;white-space:nowrap}
.benefits .bullets li::before{background:var(--white)}
.ben-left{left:10px;top:46px}
.ben-right{left:170px;top:40px}
.sub{list-style:none;padding-left:13px;margin-top:6px}
.sub li{padding-left:0;margin-bottom:6px}
.sub li::before{display:none}
.reserve{left:24px;top:304px;font-family:"Montserrat",sans-serif;font-weight:900;color:var(--red);font-size:26px;white-space:nowrap}
.reserve-line{left:24px;top:340px;font-family:"Montserrat",sans-serif;font-weight:800;color:var(--ink);font-size:16.5px;white-space:nowrap}
.call{left:24px;top:362px;font-family:"Montserrat",sans-serif;font-weight:900;color:var(--ink);font-size:25px;white-space:nowrap}
.call span{color:var(--red)}
.back-brand{left:27px;top:400px}
.supported{left:24px;top:480px;font-family:"Montserrat",sans-serif;font-weight:800;color:var(--green);font-size:13px;letter-spacing:.3px}
.partner{top:506px;height:22px;background:#8a9aa6;border-radius:4px}
.prize{left:225px;top:416px;width:160px;height:160px;border-radius:50%;background:radial-gradient(circle at 50% 40%,var(--red),var(--red-dark));border:4px solid var(--white);box-shadow:0 2px 6px rgba(0,0,0,.25);color:var(--white);font-family:"Oswald",sans-serif;font-weight:600;display:flex;flex-direction:column;align-items:center;justify-content:center;text-align:center;white-space:nowrap;overflow:hidden}
.prize .small{font-size:19px;line-height:22px;font-weight:500;letter-spacing:-.2px}
.prize .mid{font-size:29px;line-height:32px;letter-spacing:-.3px}
.prize .big{font-size:42px;line-height:44px;letter-spacing:-.3px}
</style>
</head>
<body>
<div class="canvas">

  <!-- Side one -->
  <section class="flyer flyer--front">
    <svg class="layer" width="402" height="845" viewBox="0 0 402 845">
      <defs>
        <linearGradient id="frontGreen" x1="0" y1="0" x2="1" y2="1">
          <stop offset="0" stop-color="#9acd2b"/>
          <stop offset="1" stop-color="#76b014"/>
        </linearGradient>
      </defs>
      <path d="M0 0 H170 C110 20 40 50 0 110 Z" fill="var(--green)"/>
      <path d="M170 0 H180 C110 30 40 70 0 140 V110 C40 50 110 20 170 0 Z" fill="var(--pink)"/>
      <path d="M0 480 C60 380 180 340 300 335 C350 330 385 315 402 300 V845 H0 Z" fill="var(--pink)"/>
      <path d="M0 505 C60 410 180 365 300 360 C350 356 385 340 402 325 V845 H0 Z" fill="url(#frontGreen)"/>
    </svg>
    <div class="brand abs front-brand">KINDLY NOURISH</div>
    <div class="photo fruit-photo" role="img" aria-label="Fresh strawberries, peaches, kiwi, lime and a green apple with a tape measure"></div>
    <div class="photo portrait" role="img" aria-label="Woman tossing a fresh salad in a bright kitchen"></div>
    <h1 class="abs headline">PLATE BRIGHT<br>LIVE LIVELY<br>CENTRAL COAST</h1>
    <p class="abs presenter">Presented by qualified Nutritionist</p>
    <p class="abs tagline">Food for a&nbsp; Healthir happier Life for you and your family</p>
    <div class="abs free-badge">FREE FOR NSW CENTRAL<br>COAST RESIDENTS</div>
    <p class="abs welcome">All ages welcome</p>
    <p class="abs site">
      <svg width="14" height="14" viewBox="0 0 14 14" fill="none" stroke="#fff" stroke-width="1.2"><circle cx="7" cy="7" r="6"/><ellipse cx="7" cy="7" rx="2.6" ry="6"/><path d="M1 7h12"/></svg>
      www.kindlynourish.com.au
    </p>
  </section>

  <!-- Side two -->
  <section class="flyer flyer--back">
    <svg class="layer" width="402" height="845" viewBox="0 0 402 845">
      <defs>
        <linearGradient id="foodPhoto" x1="0" y1="0" x2="1" y2="1">
          <stop offset="0" stop-color="#d9c6a6"/>
          <stop offset=".5" stop-color="#a9c0d2"/>
          <stop offset="1" stop-color="#7fa84a"/>
        </linearGradient>
      </defs>
      <path d="M0 598 C120 560 260 545 402 440 V845 H0 Z" fill="var(--pink)"/>
      <path d="M0 620 C120 578 260 565 402 462 V845 H0 Z" fill="url(#foodPhoto)" role="img" aria-label="Smiling woman eating a fresh salad at a table with vegetables and juices"/>
      <path d="M280 845 C330 810 370 770 402 720 V845 Z" fill="var(--pink)"/>
      <path d="M310 845 C350 815 380 785 402 750 V845 Z" fill="var(--green)"/>
    </svg>

    <h2 class="abs section-title learn-title">Learn About:-</h2>
    <ul class="abs bullets learn-left">
      <li>Foods that improve your health</li>
      <li>Basic nutrition</li>
      <li>Gut brain connection</li>
    </ul>
    <ul class="abs bullets learn-right">
      <li>Portion size</li>
      <li>Menu planning</li>
      <li>Preparation</li>
      <li>Eating</li>
    </ul>

    <div class="abs benefits">
      <h2 class="abs section-title benefits-title">Benefits:-</h2>
      <ul class="abs bullets ben-left">
        <li>Improved Health</li>
        <li>Improved Energy</li>
        <li>Family fun</li>
      </ul>
      <ul class="abs bullets ben-right">
        <li>Manage Chronic Illness
          <ul class="sub">
            <li>o Diabetes Type II</li>
            <li>o Cholesterol</li>
            <li>o Blood Pressure</li>
          </ul>
        </li>
      </ul>
    </div>

    <p class="abs reserve">Reserve for</p>
    <p class="abs reserve-line">spot online @ www.platebright.com.au</p>
    <p class="abs call"><span>Call</span> 0462 508 731</p>

    <div class="brand abs back-brand">KINDLY NOURISH</div>
    <p class="abs supported">SUPPORTED BY :-</p>
    <div class="abs partner" style="left:24px;width:46px" role="img" aria-label="Harbourline Shire Council badge"></div>
    <div class="abs partner" style="left:92px;width:64px" role="img" aria-label="Harbourline Rugby Social Club badge"></div>
    <div class="abs partner" style="left:176px;width:38px" role="img" aria-label="Pindara Veterans Club badge"></div>

    <div class="abs prize">
      <div class="small">FOOD TASTINGS</div>
      <div class="mid">LUCKY DOOR</div>
      <div class="big">PRIZE</div>
    </div>
  </section>

</div>
</body>
</html>
```